Business card design for a debt inventory management software company

We need a business card design to help us move into the next phase of our business. We developed an innovative solution to help companies collect their bad debts. We are moving into a new era and branching out into new industries. We are open to design ideas but would like that they have a similar feel/look to our website and include our logo. https://www.lumoryx.com

Target Market(s)

Finance Industry, Telecom Industry, Utility Industry, Healthcare Industry, Insurance Industry

Industry/Entity Type

Software

Contact Information for Business Card

Include Name, Title, Phone, Email, website, address, and logo

Font styles to use
Sans Serif

Colors

Designer to choose colors to be used in the design.

Requirements
Must have
• A similar look and feel to our website. https://www.lumoryx.com

```html
<!DOCTYPE html>
<html lang="en">
<head>
<meta charset="utf-8">
<title>Lumoryx Software – Business Card</title>
<link href="https://fonts.googleapis.com/css2?family=Montserrat:wght@300&family=Arimo:wght@400;700&display=swap" rel="stylesheet">
<style>
  :root {
    --stage: #3b3b3d;
    --navy: #384369;
    --navy-ink: #1f2f7a;
    --paper: #e6e6e6;
    --ink: #1c1c1c;
    --grey-rule: #555;
    --green: #7fa43a;
    --white: #ffffff;
  }
  * { box-sizing: border-box; margin: 0; padding: 0; }
  html, body { width: 1200px; height: 1000px; overflow: hidden; }
  body {
    background: var(--stage);
    font-family: "Arimo", Arial, sans-serif;
    position: relative;
  }
  .card {
    position: absolute;
    left: 270px;
    width: 660px;
    height: 380px;
    border-radius: 26px;
    overflow: hidden;
  }
  .card--back { top: 50px; background: var(--navy); }
  .card--front { top: 540px; background: var(--paper); }

  .brand {
    position: absolute;
    font-family: "Montserrat", sans-serif;
    font-weight: 300;
    white-space: nowrap;
    display: flex;
    align-items: center;
    gap: 14px;
  }
  .brand__dot { width: 34px; height: 34px; border-radius: 50%; }
  .card--back .brand {
    left: 0; right: 0; top: 160px;
    justify-content: center;
    font-size: 46px;
    color: var(--white);
  }
  .card--back .brand__dot { background: var(--white); }
  .card--front .brand {
    left: 0; right: 0; top: 40px;
    justify-content: center;
    font-size: 42px;
    color: var(--navy-ink);
  }
  .card--front .brand__dot { background: var(--navy-ink); }

  .person {
    position: absolute;
    left: 0; right: 0; top: 150px;
    text-align: center;
  }
  .person__name {
    font-weight: 700;
    font-size: 26px;
    letter-spacing: 0.5px;
    color: var(--navy-ink);
  }
  .person__title {
    font-size: 15px;
    color: var(--ink);
    margin-top: 2px;
  }
  .details {
    position: absolute;
    top: 232px; left: 0; right: 0;
    display: flex;
    justify-content: center;
    font-size: 16px;
    color: var(--ink);
    line-height: 1.35;
  }
  .details__col { padding: 0 22px; }
  .details__col--left { text-align: right; }
  .details__rule { width: 1.5px; background: var(--grey-rule); }
  .details__line { display: flex; align-items: center; gap: 8px; }
  .details__col--left .details__line { justify-content: flex-end; }
  .details__line svg { width: 14px; height: 14px; flex: none; fill: none; stroke: #333; stroke-width: 1.6; }
  .details__web strong { font-weight: 700; }
  .band {
    position: absolute;
    left: 0; right: 0; bottom: 0;
    height: 26px;
    background: var(--green);
  }
</style>
</head>
<body>

<section class="card card--back" aria-label="Card back">
  <div class="brand"><span class="brand__dot"></span>Lumoryx Software</div>
</section>

<section class="card card--front" aria-label="Card front">
  <div class="brand"><span class="brand__dot"></span>Lumoryx Software</div>

  <div class="person">
    <div class="person__name">DANIEL REYES</div>
    <div class="person__title">Executive Assistant</div>
  </div>

  <div class="details">
    <div class="details__col details__col--left">
      <div>240 Brookfield Avenue,</div>
      <div>Suite 310, Dalton, Ohio 44618</div>
      <div class="details__line details__web">
        <svg viewBox="0 0 16 16"><circle cx="8" cy="8" r="6.5"/><path d="M1.5 8h13M8 1.5c-3 3.5-3 9.5 0 13M8 1.5c3 3.5 3 9.5 0 13"/></svg>
        <span>www.<strong>lumoryx</strong>.com</span>
      </div>
    </div>
    <div class="details__rule"></div>
    <div class="details__col details__col--right">
      <div class="details__line">
        <svg viewBox="0 0 16 16"><path d="M3 2h3l1.5 3.5-2 1.3a8 8 0 0 0 3.7 3.7l1.3-2L14 10v3a1.5 1.5 0 0 1-1.5 1.5A11 11 0 0 1 1.5 3.5 1.5 1.5 0 0 1 3 2z"/></svg>
        <span>330.555.0142</span>
      </div>
      <div class="details__line">
        <svg viewBox="0 0 16 16"><rect x="4" y="1.5" width="8" height="4"/><rect x="1.5" y="5.5" width="13" height="6" rx="1"/><rect x="4" y="9.5" width="8" height="5"/></svg>
        <span>330.555.0187</span>
      </div>
      <div class="details__line">
        <svg viewBox="0 0 16 16"><rect x="1.5" y="3.5" width="13" height="9" rx="1"/><path d="M1.5 4l6.5 5 6.5-5"/></svg>
        <span>info@lumoryx.com</span>
      </div>
    </div>
  </div>

  <div class="band"></div>
</section>

</body>
</html>
```